Mobile Repair Service on location needs a Web Design

We are starting a new mobile device repair service called Gadget Haven and our website needs a design!

Hello Designers!
First, we'd like to make clear this is more than a simple web design contest, we want the designers to create an idea. We want someone who can create the whole theme of the service's we provide. We want someone that can help design our visual branding, help us communicate a sentiment. And we are willing to pay for that.

Who are we?
Our company is based in Rotterdam, the Netherlands. We provide different services for all kinds of electronic devices. The kind of services we provide are, among other things, installations of hardware and software and the repair of broken or malfunctioning devices.
We are starting a new service that offers mobile device repairs on location, be it at the home of our customers, their office, or any other place. Just give us the address and we will come to you for the repair job. This is also our main USP. We have multiple skilled engineers who drive trough the country on a daily basis and can be on location within a working day. Repair is done immediately onsite while the customer waits. At this stage we will start with the smartphone product-group within the mobile devices. In a second phase we might also add tablets.
People don't want to be without their phone for weeks because of some parts that needed to be ordered by a repair center they had to sent their phone to. We offer a fully functional mobile repair center in the form of specially customized vans. These vans have all the tools and utilities needed by our engineers to safely repair your mobile device. Your phone is being repaired directly in front of you, the next business-day, on a location you desire.

For this new service we are creating a website called Gadget Haven. The website needs a story and matching design and this is where you come in. We are not looking for a simple template design we can get from any place. We need a story. We want you to create an idea, build a unique theme or vision that helps sell the product/service. This goes beyond the design of the website. We need the whole package, the design you are creating needs to have returning elements like icons, color use, images, maybe even characters etc. You name it! There needs to be a common thread in the design so we can reuse elements in, for example, the email templates, the work order or receipt we give to our customers (we may contact the winner of the contest to design these for us as well!).

The name 'Gadget Haven' is chosen. Haven (short for rehabilitate) has a bold and playful tone to it and the design needs to reflect the name. So we're looking for a somewhat playful and cheeky design. Definitely not too serious and definitely modern. We already got a logo that we love and that fit's this description (see attached design documents for the logo). It's bold, powerful and fun. Our web design needs to reflect this as well and has to fit in with our logo.
We would really like it if the design somehow incorporates elements that highlight our unique selling points (repairs on location, we come to you etc.). We would really like some form of story telling in the design. Think clumsy people breaking their phones. Teenagers in tears because they have no access to their friends. People nowadays have the need to always be 'connected'. What happens when your phone is broken or malfunctioning? We're handling tech, we are nerds and a little bit weird, but we're professionals and here to help you with your problem. The sentiment Wire Troop tries to communicate is something we really like. We're looking for fresh idea's, anything goes!

In an overview all Unique Selling Points of the Gadget haven service:
- Professional service on location. Don’t ship to us we will come to you!
- Clear pricing upfront. No hidden cost.
- Next business-day repair.
- Backed by a professional call center open 12 hours a day and open on a Saturday as well
- Backed by a professional repair center with more then 12 years of experience
- Repair is done by certified engineers
- 1 year warranty on the repair

The process:
The main function of our website will be for customers to make a repair request. A customer will visit our website and can make a repair request immediately by going through a 'request-order-flow'. In this flow he or she will need to fill in some forms and can select wich type/model/brand of mobile device he or she has and what parts need to be repaired. After a request is placed we will call the customer back (within an hour) for a short intake and to set a date/time and location. Our engineer will meet the customer at the specified location and will repair the device onsite in one of our mobile repair centers, which is a specialized van equipped with all the tools needed for device restorations.
So in short the steps are:
- Choose your device and repair job
- Place the order
- Get a callback within the hour
- Set date and location
- We will come to you.

Website functionality:
Our website is our main form of communication. So the sentiment we want to communicate needs be reflected in the design. We need a main/front page designed (preferably a long scrolling page design) containing:
1. Customers will be able to request a repair job directly on our website. So there will need to be a prominent button/link at the top of our main page that will bring the customer to this 'request-order-flow'. This is the main flow which needs to be full focus on the front page. All other items are secondary.
2. The general information of who we are and what we do, and why the customer should choose us. Preferably in short bullet-point type keywords/sentences with icons or other visual cues. See our unique selling points to get an idea of the information that will be displayed here.
3. There needs to be a section that will explain the process (see above) of a repair request step-by- step, again in brief short key sentences and with (custom) icons.
4. There needs to be a section that explains to the customer he/she can always contact us if they are not sure what the problem is with their device, and for this reason are not sure what repair request they should order.
5. We want to implement some functionality that display customer ratings or customer reviews. So there needs to be room for some kind of widget of plugin we're going to implement which shows these reviews.
6. A 'For business section' where we will explain all the options we provide for corporate clients.
7. Social media links.
8. There needs to be a menu with buttons that leads to the all sections described in the previous points.

For now, we need a design for our front page. In the second phase, when we have picked our winner, we may ask the winner to design the page(s) for our request workflow as well.

EDIT:
Finally, we have a very specific order in mind for the different segments of our website. We would like you to add some more segments that were not in our original brief as well:

1. Top header with order/request button. (should instantly make clear our main USP, we do repairs on location)
2. Our process
3. Our unique selling points / why choose us
4. The kind of repairs we do (broken screens, broken batteries, water damage, broken camera's, no sound etc.)
5. A 'meet our team' section, where we introduce some of our engineers
6. A 'contact us for any questions' section/
7. Testimonials/user reviews
8. A section where we show key performance indicators
9. 'For businesses' sections
10.'Subscribe for newsletter' field
11. Social media buttons

Industry/Entity Type

It Service

Number of Pages Required

1 page

Font styles to use
Sans Serif

Requirements
Must have
• a main/front page, design only
• custom icons/images for banners, adverts online and in print (high res)
Nice to have
• Storytelling in our design.
• Design that fits with our brand new logo.
• Elements like icons to have a flat design.
• Keep in mind that the website will need to be responsive when designing! (Ideally provide an example of the mobile design as well)
• Create a fun and trustworthy feeling.

```html
<!DOCTYPE html>
<html lang="en">
<head>
<meta charset="utf-8">
<title>Gadget Haven – Repairs on Location</title>
<link rel="stylesheet" href="https://fonts.googleapis.com/css2?family=Open+Sans:ital,wght@0,400;0,600;0,700;0,800;1,400&display=swap">
<style>
:root{
  --orange:#f26322;
  --lavender:#dfddef;
  --lavender-mid:#c6c3e2;
  --quote:#bcb8dc;
  --ink:#25313a;
  --body:#4a4f5c;
  --charcoal:#404040;
  --charcoal-dark:#353535;
  --white:#ffffff;
  --muted:#a8a8a8;
}
*{box-sizing:border-box;margin:0;padding:0}
html,body{width:1200px;height:3030px;overflow:hidden}
body{position:relative;background:var(--white);font-family:"Open Sans",Arial,sans-serif;color:var(--ink)}
.abs{position:absolute}

/* Header */
.topbar{left:0;top:0;width:1200px;height:66px;background:var(--lavender);z-index:3}
.nav{top:0;height:66px;display:flex;align-items:center;gap:26px;font-size:13px;font-weight:700;letter-spacing:.3px;color:var(--ink);z-index:5}
.nav-left{left:110px}
.nav-right{left:792px}
.btn-order{left:958px;top:12px;width:132px;height:38px;background:var(--orange);color:var(--white);font-size:12.5px;font-weight:700;display:flex;align-items:center;justify-content:center;z-index:5}
.brand-tab{left:470px;top:0;width:298px;height:140px;z-index:4}
.brand{left:500px;top:22px;width:240px;display:flex;align-items:center;justify-content:center;gap:12px;z-index:6}
.brand-dot{width:52px;height:52px;border-radius:50%;background:var(--orange);flex:none}
.brand-name{font-size:25px;font-weight:800;line-height:1;color:var(--charcoal)}
.brand-tag{font-size:10px;font-weight:700;color:#4d55a8;margin-top:4px}

/* Hero */
.hero{left:0;top:66px;width:1200px;height:490px;overflow:hidden}
.hero-photo{left:0;top:0;width:1200px;height:490px;background:linear-gradient(90deg,#3d5e9c 0%,#6e86b9 14%,#d9cec4 30%,#efe7de 48%,#d8d2c6 70%,#c8c0b2 100%)}
.hero-band{left:0;top:318px;width:600px;height:110px;background:rgba(255,255,255,.55)}
.hero-title{left:111px;top:330px;font-size:34px;font-weight:800;line-height:1.02;color:var(--ink);text-transform:uppercase}
.dots{left:580px;top:470px;display:flex;gap:9px}
.dots span{width:7px;height:7px;border-radius:50%;background:var(--white)}
.dots span:first-child{background:#d9d9d9}

.contact-card{left:750px;top:140px;width:276px;height:350px;background:var(--charcoal);box-shadow:0 6px 16px rgba(0,0,0,.35);z-index:2}
.contact-badge{left:854px;top:108px;width:68px;height:50px;z-index:3}
.contact-title{left:750px;top:154px;width:276px;text-align:center;color:var(--white);font-size:16px;font-weight:700;z-index:3}
.field{left:760px;width:256px;height:42px;background:var(--white);border:1px solid #cfcfcf;font-size:12px;color:#b3b3b3;padding:12px 10px;z-index:3}
.field-area{height:94px}
.form-btn{left:796px;top:436px;width:184px;height:40px;background:var(--lavender-mid);color:var(--ink);font-size:12.5px;font-weight:700;display:flex;align-items:center;justify-content:center;z-index:3}

/* About */
.about-photo{left:155px;top:606px;width:316px;height:316px;border-radius:50%;border:3px solid #a7a3d2;background:radial-gradient(circle at 45% 45%,#eef1f4 0%,#b9c2cb 45%,#5d6b78 100%)}
.about-title{left:517px;top:668px;font-size:34px;font-weight:800;color:var(--ink)}
.about-text{left:517px;top:724px;width:540px;font-size:14px;line-height:25px;color:var(--body)}
.btn-more{left:519px;top:854px;width:106px;height:38px;background:var(--orange);color:var(--white);font-size:12.5px;font-weight:700;display:flex;align-items:center;justify-content:center}

/* Section headings */
.section-title{left:0;width:1200px;text-align:center;font-size:35px;font-weight:800;color:var(--ink)}

/* Why us */
.usp-band{left:0;top:940px;width:1200px;height:460px}
.feature{width:200px;text-align:center}
.feature svg{display:block;margin:0 auto}
.feature-label{margin-top:14px;font-size:16px;font-weight:600;color:#333;transform:rotate(-4deg)}

/* What we do */
.service-card{top:1515px;width:477px;height:269px;overflow:hidden}
.service-photo{left:0;top:0;width:100%;height:100%}
.service-caption{left:0;top:182px;width:100%;height:87px;background:rgba(58,58,58,.85);color:var(--white);font-size:26px;font-weight:700;line-height:1.02;text-align:center;display:flex;align-items:center;justify-content:center;text-transform:uppercase}

/* Process */
.process-band{left:0;top:1880px;width:1200px;height:460px}
.step{width:200px;text-align:center;color:var(--white)}
.step svg{display:block;margin:0 auto}
.step-label{margin-top:10px;font-size:15px;font-weight:800;line-height:1.15;transform:rotate(-4deg)}

/* Testimonials */
.quote-mark{top:2370px;font-size:250px;font-weight:800;line-height:1;color:var(--quote);font-family:Georgia,"Times New Roman",serif}
.testimonial-title{left:0;top:2422px;width:1200px;text-align:center;font-size:36px;font-weight:700;color:var(--ink)}
.testimonial-photo{left:273px;top:2535px;width:162px;height:162px;border-radius:50%;background:radial-gradient(circle at 50% 40%,#d9c9b6 0%,#a68f79 55%,#6b5a4c 100%)}
.testimonial-text{left:459px;top:2545px;width:470px;font-size:15px;line-height:26px;font-style:italic;color:var(--body)}
.testimonial-name{left:459px;top:2657px;font-size:17px;font-weight:600;color:var(--orange)}

/* Footer */
.footer{left:0;top:2814px;width:1200px;height:216px;background:var(--charcoal)}
.footer-tab{left:479px;top:2741px;width:242px;height:75px}
.footer-brand{left:479px;top:2766px;width:242px;display:flex;align-items:center;justify-content:center;gap:10px}
.footer-brand .brand-dot{width:34px;height:34px}
.footer-brand .brand-name{font-size:18px;color:var(--white)}
.footer-nav{left:0;top:2851px;width:1200px;display:flex;justify-content:center;gap:30px;font-size:12px;font-weight:600;color:#e4e4e4}
.social{left:0;top:2891px;width:1200px;display:flex;justify-content:center;gap:6px}
.social span{width:26px;height:26px;border-radius:50%}
.copyright{left:0;top:2985px;width:1200px;text-align:center;font-size:11px;color:#8a8a8a}
</style>
</head>
<body>

<!-- Header -->
<div class="abs topbar"></div>
<nav class="abs nav nav-left"><span>HOME</span><span>ABOUT</span><span>WHAT WE DO</span><span>OUR PROCESS</span></nav>
<nav class="abs nav nav-right"><span>WHY US</span><span>CONTACT</span></nav>
<div class="abs btn-order">PLACE AN ORDER</div>
<svg class="abs brand-tab" viewBox="0 0 298 140" aria-hidden="true"><polygon points="0,0 298,0 250,118 149,140 48,118" fill="#ffffff"/></svg>
<div class="abs brand">
  <span class="brand-dot"></span>
  <div><div class="brand-name">GADGET<br>HAVEN</div><div class="brand-tag">We will come to you!</div></div>
</div>

<!-- Hero -->
<section class="abs hero">
  <div class="abs hero-photo" role="img" aria-label="Photo of a repair technician in blue overalls beside a smiling couple"></div>
  <svg class="abs" style="left:0;top:0" width="1200" height="490" aria-hidden="true">
    <path d="M1200 155 C1120 260 980 390 820 430 L300 490 L1200 490 Z" fill="#f26322"/>
  </svg>
  <div class="abs hero-band"></div>
  <h1 class="abs hero-title">Repairs on location,<br>we come to you</h1>
  <div class="abs dots"><span></span><span></span><span></span></div>
</section>

<div class="abs contact-card"></div>
<svg class="abs contact-badge" viewBox="0 0 68 50" aria-hidden="true"><path d="M0 50 A34 34 0 0 1 68 50 Z" fill="#404040"/><circle cx="34" cy="26" r="11" fill="#f26322"/></svg>
<div class="abs contact-title">CONTACT US</div>
<div class="abs field" style="top:186px">Name</div>
<div class="abs field" style="top:234px">Phone</div>
<div class="abs field" style="top:282px">Email</div>
<div class="abs field field-area" style="top:330px">Complaints</div>
<div class="abs form-btn">PLACE AN ORDER</div>

<!-- About -->
<div class="abs about-photo" role="img" aria-label="Close-up photo of gloved hands repairing a smartphone on a workbench"></div>
<h2 class="abs about-title">GADGET HAVEN</h2>
<p class="abs about-text">Lorem ipsum dolor sit amet, consectetur adipiscing elit, sed do eiusmod tempor incididunt ut labore et dolore magna aliqua. Ut enim ad minim veniam, quis. Lorem ipsum dolor sit amet, consectetur adipiscing elit, sed do eiusmod tempor incididunt ut labore et dolore magna aliqua.</p>
<div class="abs btn-more">KNOW MORE</div>

<!-- Why us -->
<svg class="abs usp-band" viewBox="0 0 1200 460" aria-hidden="true">
  <polygon points="0,10 1200,65 1200,410 0,440" fill="#dfddef"/>
  <polygon points="0,440 1200,410 1200,416 0,446" fill="#f26322"/>
</svg>
<h2 class="abs section-title" style="top:1058px">WHY US?</h2>

<div class="abs feature" style="left:90px;top:1132px">
  <svg width="60" height="70" viewBox="0 0 60 70" fill="none" stroke="#f26322" stroke-width="3"><path d="M30 60 C14 40 10 32 10 24 A20 20 0 0 1 50 24 C50 32 46 40 30 60Z"/><circle cx="30" cy="24" r="8"/><ellipse cx="30" cy="64" rx="18" ry="4"/></svg>
  <div class="feature-label">Service On Location</div>
</div>
<div class="abs feature" style="left:298px;top:1132px">
  <svg width="90" height="70" viewBox="0 0 90 70" fill="none" stroke="#f26322" stroke-width="3"><path d="M5 35 C22 12 68 12 85 35 C68 58 22 58 5 35Z"/><circle cx="45" cy="35" r="11"/><line x1="22" y1="62" x2="68" y2="8"/></svg>
  <div class="feature-label">No Hidden Cost</div>
</div>
<div class="abs feature" style="left:502px;top:1132px">
  <svg width="70" height="70" viewBox="0 0 70 70" fill="none" stroke="#f26322" stroke-width="3"><circle cx="22" cy="12" r="7"/><path d="M14 24 L14 46 L36 46 L36 64"/><path d="M8 30 L8 52 L28 52 L28 64"/><circle cx="52" cy="20" r="12"/><path d="M52 13 V20 H58"/></svg>
  <div class="feature-label">No Waiting</div>
</div>
<div class="abs feature" style="left:708px;top:1132px">
  <svg width="60" height="70" viewBox="0 0 60 70" fill="none" stroke="#f26322" stroke-width="3"><path d="M18 4 L26 28 M42 4 L34 28"/><circle cx="30" cy="46" r="18"/><circle cx="30" cy="46" r="10"/></svg>
  <div class="feature-label">12 Years Experience</div>
</div>
<div class="abs feature" style="left:920px;top:1132px">
  <svg width="64" height="70" viewBox="0 0 64 70" fill="none" stroke="#f26322" stroke-width="3"><circle cx="32" cy="28" r="22"/><circle cx="32" cy="28" r="13"/><path d="M18 46 L12 66 L22 60 L28 68 L30 50 M46 46 L52 66 L42 60 L36 68 L34 50"/></svg>
  <div class="feature-label">1 Years Warranty</div>
</div>

<!-- What we do -->
<h2 class="abs section-title" style="top:1430px">WHAT WE DO</h2>
<div class="abs service-card" style="left:111px">
  <div class="abs service-photo" role="img" aria-label="Greyscale photo of hands typing on a keyboard with digital overlays" style="background:linear-gradient(160deg,#e6e6e6 0%,#9c9c9c 45%,#3b3b3b 100%)"></div>
  <div class="abs service-caption">Installations of<br>hardware &amp; software</div>
</div>
<div class="abs service-card" style="left:612px">
  <div class="abs service-photo" role="img" aria-label="Greyscale photo of a smartphone with a shattered screen" style="background:linear-gradient(200deg,#d8d8d8 0%,#a6a6a6 50%,#5a5a5a 100%)"></div>
  <div class="abs service-caption">Reapir of<br>broken devices</div>
</div>

<!-- Process -->
<svg class="abs process-band" viewBox="0 0 1200 460" aria-hidden="true">
  <polygon points="0,15 1200,75 1200,82 0,22" fill="#c6c3e2"/>
  <polygon points="0,15 1200,80 1200,400 0,447" fill="#f26322"/>
</svg>
<h2 class="abs section-title" style="top:1995px">OUR PROCESS</h2>

<div class="abs step" style="left:94px;top:2072px">
  <svg width="70" height="76" viewBox="0 0 70 76" fill="none" stroke="#2b2b2b" stroke-width="3"><rect x="18" y="4" width="28" height="48" rx="4"/><line x1="28" y1="44" x2="36" y2="44"/><path d="M12 40 C4 52 10 66 26 70 L48 70 C58 62 60 52 54 46 L40 50"/></svg>
  <div class="step-label">Choose Your Device<br>&amp; Job</div>
</div>
<div class="abs step" style="left:286px;top:2076px">
  <svg width="72" height="72" viewBox="0 0 72 72" fill="none" stroke="#2b2b2b" stroke-width="3"><circle cx="36" cy="36" r="32"/><path d="M22 37 L32 47 L52 25"/></svg>
  <div class="step-label">Place The Order</div>
</div>
<div class="abs step" style="left:480px;top:2076px">
  <svg width="72" height="72" viewBox="0 0 72 72" fill="none" stroke="#2b2b2b" stroke-width="3"><path d="M14 10 L26 10 L30 24 L22 30 C26 40 32 46 42 50 L48 42 L62 46 L62 58 C40 62 10 32 14 10Z"/><path d="M40 16 A16 16 0 0 1 56 32 M40 6 A26 26 0 0 1 66 32"/></svg>
  <div class="step-label">Get a Callback<br>Within The Hour</div>
</div>
<div class="abs step" style="left:704px;top:2076px">
  <svg width="72" height="72" viewBox="0 0 72 72" fill="none" stroke="#2b2b2b" stroke-width="3"><rect x="10" y="14" width="52" height="50" rx="3"/><line x1="10" y1="26" x2="62" y2="26"/><line x1="22" y1="8" x2="22" y2="18"/><line x1="50" y1="8" x2="50" y2="18"/><path d="M26 44 L33 51 L47 37"/></svg>
  <div class="step-label">Set Date &amp;<br>Location</div>
</div>
<div class="abs step" style="left:914px;top:2076px">
  <svg width="86" height="72" viewBox="0 0 86 72" fill="none" stroke="#2b2b2b" stroke-width="3"><path d="M6 52 L6 18 L54 18 L54 52"/><path d="M54 28 L70 28 L80 42 L80 52 L6 52"/><circle cx="22" cy="56" r="7" fill="#f26322"/><circle cx="66" cy="56" r="7" fill="#f26322"/></svg>
  <div class="step-label">We Will Come<br>to You</div>
</div>

<!-- Testimonials -->
<div class="abs quote-mark" style="left:122px">&ldquo;</div>
<div class="abs quote-mark" style="left:940px">&rdquo;</div>
<h2 class="abs testimonial-title">WHAT OUR CUSTOMERS HAVE TO SAY</h2>
<div class="abs testimonial-photo" role="img" aria-label="Portrait photo of a happy customer couple"></div>
<p class="abs testimonial-text">Lorem ipsum dolort amet, consectetur adipiscing elit, sed do eiusmod tempor incididunt ut labore dolore magna aliqua ipsum dolor sit consectetur. Adipiscing elit, sed do eiusmod tempor incididunt ut labore.</p>
<div class="abs testimonial-name">Milo &amp; Vera</div>

<!-- Footer -->
<footer class="abs footer"></footer>
<svg class="abs footer-tab" viewBox="0 0 242 75" aria-hidden="true"><polygon points="44,0 198,0 242,75 0,75" fill="#404040"/></svg>
<div class="abs footer-brand"><span class="brand-dot"></span><span class="brand-name">GADGET HAVEN</span></div>
<nav class="abs footer-nav"><span>HOME</span><span>ABOUT</span><span>WHAT WE DO</span><span>OUR PROCESS</span><span>WHY US</span><span>TESTIMONIALS</span><span>CONTACT</span></nav>
<div class="abs social" aria-label="Social media links"><span style="background:#3b5b9a"></span><span style="background:#2aa3e0"></span><span style="background:#d84a38"></span></div>
<div class="abs copyright">Copyright 2017 © Gadget Haven | All rights reserved</div>

</body>
</html>
```